Design Footer or Header for Pizza Restaurant Menu

-Design a footer or header using our logo and contact information.
-The menu items in the middle should be exactly as shown in the .psd examples.
-2 Pages (both should have the same design of Footer or Header)
-Menu Items (Document Link)
https://sheets.brindlework.com/tables/d/7QpXa2mR9vLt4KwZ8nHc3YeB6uJf1DsG5oNi0TzWr2Kx/edit?usp=sharing
Contact Information
8157 Tarrowell Avenue, Alder Ridge, NY 12831
847-318-5037
Ovenbellhub.com

```html
<!DOCTYPE html>
<html lang="en">
<head>
<meta charset="utf-8">
<title>Ovenbell Menu – Two Pages</title>
<link href="https://fonts.googleapis.com/css2?family=Arimo:wght@400;500;700&family=Kaushan+Script&family=Oswald:wght@300;500;600&display=swap" rel="stylesheet">
<style>
  :root{
    --red:#e0121c;
    --red-deep:#b7000b;
    --red-dark:#8c0710;
    --ink:#1e1e1e;
    --muted:#8d8d8d;
    --paper:#fbf9f4;
    --black:#111111;
    --backdrop:#c9c8c6;
    --white:#ffffff;
  }
  *{box-sizing:border-box;margin:0;padding:0}
  html,body{width:1200px;height:2912px;overflow:hidden}
  body{background:var(--backdrop);font-family:'Arimo',Arial,sans-serif;color:var(--ink);position:relative}

  .menu-page{position:absolute;left:170px;width:860px;height:1340px;background:var(--paper);overflow:hidden;box-shadow:0 6px 18px rgba(0,0,0,.25)}
  .menu-page--food{top:75px}
  .menu-page--pizza{top:1497px}

  .page-header{position:absolute;inset:0 0 auto 0;height:250px}
  .header-band{position:absolute;left:0;top:0;width:860px;height:250px}
  .brand-name{position:absolute;left:38px;top:68px;font-family:'Kaushan Script',cursive;font-size:60px;color:var(--white);line-height:1}
  .menu-title{position:absolute;left:318px;top:22px;font-family:'Kaushan Script',cursive;font-size:108px;color:var(--white);line-height:1}
  .pizza-kicker{position:absolute;left:392px;top:28px;font-family:'Kaushan Script',cursive;font-size:46px;color:var(--white);line-height:1}
  .pizza-title{position:absolute;left:308px;top:72px;font-family:'Arimo',sans-serif;font-weight:700;font-size:100px;color:var(--white);line-height:1;letter-spacing:-1px}
  .food-photo{position:absolute;border-radius:50%}
  .food-photo--spread{left:580px;top:18px;width:280px;height:205px;background:radial-gradient(ellipse at 55% 55%,#e3a04a 0%,#d9c9a6 38%,rgba(176,60,20,.55) 62%,rgba(200,20,25,0) 75%)}
  .food-photo--pizza{left:595px;top:40px;width:265px;height:205px;background:radial-gradient(ellipse at 45% 62%,#f0b54c 0%,#d5632a 36%,rgba(120,30,15,.6) 58%,rgba(200,20,25,0) 74%)}

  .menu-section{position:absolute}
  .section-title{font-weight:700;color:var(--red);font-size:17px;text-align:center;letter-spacing:.3px;margin-bottom:4px}
  .section-note{font-weight:700;color:var(--red);font-size:8px;text-align:center;margin-top:-3px;margin-bottom:10px}
  .section-title + .item{margin-top:14px}

  .item{margin-bottom:7px}
  .item-head{display:flex;align-items:baseline;font-size:12.5px;font-weight:500;text-transform:uppercase;color:var(--ink)}
  .item-leader{flex:1;border-bottom:1px dotted #555;margin:0 2px;transform:translateY(-2px)}
  .item-price{white-space:nowrap}
  .item-price small{font-size:6.5px;margin:0 1px}
  .item-desc{font-size:8.3px;line-height:1.15;color:var(--muted);text-transform:uppercase;margin-top:1px}

  .pizza-list .item{margin-bottom:5.5px}
  .topping-list .item{margin-bottom:9.8px}
  .dessert-list .item{margin-bottom:12px}
  .dessert-list .item-desc{font-size:11px;color:var(--ink);margin-top:2px}

  .add-ons{position:absolute;left:32px;top:1085px;width:380px;display:flex;justify-content:center}
  .add-on{width:150px;text-align:center;font-size:8.5px;font-weight:700;text-transform:uppercase;line-height:1.3}
  .add-on + .add-on{border-left:1px solid #888}
  .add-on-title{color:var(--red);font-size:11px;margin-bottom:6px}
  .add-on-title sup{font-size:7px}

  .feature-box{position:absolute;left:445px;top:558px;width:383px;height:113px;border:2px solid var(--red);border-radius:5px;text-align:center;font-family:'Oswald',sans-serif;padding-top:4px}
  .feature-title{color:var(--red);font-weight:600;font-size:17px;letter-spacing:.5px}
  .feature-style{font-weight:300;font-size:10.5px;color:var(--ink);margin-top:2px}
  .feature-prices{font-weight:500;font-size:18px;letter-spacing:1.5px;color:#333;line-height:1.25;margin-top:4px}
  .feature-prices sup{font-size:9px}
  .feature-sub{font-weight:300;font-size:8px;color:#333}

  .page-footer{position:absolute;left:0;bottom:0;width:860px;height:180px}
  .footer-band{position:absolute;inset:0}
  .contact-row{position:absolute;left:35px;right:35px;top:77px;display:flex;align-items:center;justify-content:space-between;color:var(--white);font-size:17px}
  .contact-row .phone{color:var(--red)}
  .contact-item{display:flex;align-items:center;gap:8px}
  .contact-icon{width:15px;height:15px;flex:none}
  .hours{position:absolute;left:290px;top:112px;width:280px;height:34px;background:var(--red);clip-path:polygon(2% 18%,10% 4%,30% 12%,50% 0,72% 10%,92% 2%,100% 30%,97% 70%,100% 96%,78% 88%,55% 100%,32% 90%,10% 100%,0 78%,3% 50%);display:flex;align-items:center;justify-content:center;gap:6px;font-weight:700;font-size:15px}
  .hours-days{color:var(--red-dark)}
  .hours-time{color:var(--white)}
</style>
</head>
<body>

<!-- Page one: appetizers, salads, panini and entrees -->
<section class="menu-page menu-page--food">
  <header class="page-header">
    <svg class="header-band" viewBox="0 0 860 250" aria-hidden="true">
      <defs>
        <linearGradient id="redFood" x1="0" y1="0" x2="1" y2="1">
          <stop offset="0" stop-color="#c8000c"/><stop offset=".5" stop-color="#e31520"/><stop offset="1" stop-color="#b5000a"/>
        </linearGradient>
      </defs>
      <path fill="url(#redFood)" d="M0 0H860V170L830 180 800 174 770 190 740 182 700 198 660 190 620 204 580 196 540 210 500 202 460 216 420 206 380 222 340 212 300 228 260 218 220 232 180 222 140 238 100 228 60 244 30 234 0 248Z"/>
      <path fill="#fbf9f4" d="M120 236L240 212 238 216 126 240Z M420 210L560 192 556 196 424 214Z M640 194L760 178 758 182 644 198Z"/>
    </svg>
    <div class="brand-name">Ovenbell</div>
    <div class="menu-title">Menu</div>
    <div class="food-photo food-photo--spread" role="img" aria-label="Photo of penne pasta, fried chicken nuggets and a wrap"></div>
  </header>

  <div class="menu-section" style="left:32px;top:250px;width:380px">
    <h2 class="section-title">APPETIZERS</h2>
    <div class="item"><div class="item-head"><span>Homemade Mozzarella Sticks (5)</span><span class="item-leader"></span><span class="item-price">$10.50</span></div><p class="item-desc">Smoked mozzarella chunky sticks coated in breadcrumbs served with spicy tomato sauce</p></div>
    <div class="item"><div class="item-head"><span>Homemade Chicken Nuggets (6)</span><span class="item-leader"></span><span class="item-price">$9.50</span></div><p class="item-desc">Real homemade chicken nuggets (local farm raised chicken) served w/ french fries</p></div>
    <div class="item"><div class="item-head"><span>Roasted Chicken Wings (6) (12)</span><span class="item-leader"></span><span class="item-price">$9.00/$16.00</span></div><p class="item-desc">Seasoned available in our homemade buffalo sauce, garlic &amp; romano cheese, hickory smoked BBQ, honey BBQ, cajun dry rub, sweet chili sauce</p></div>
    <div class="item"><div class="item-head"><span>Polpette (Meatballs) (5)</span><span class="item-leader"></span><span class="item-price">$10.50</span></div><p class="item-desc">Homemade baked meatballs in rich tomato sauce with whipped buffalo ricotta</p></div>
    <div class="item"><div class="item-head"><span>Firecracker Calamari</span><span class="item-leader"></span><span class="item-price">$14.00</span></div><p class="item-desc">Crispy fried calamari with cherry peppers served with lemon aioli and marinara (your choice of spicy &amp; not spicy)</p></div>
    <div class="item"><div class="item-head"><span>Crocchette di Patate (5)</span><span class="item-leader"></span><span class="item-price">$9.50</span></div><p class="item-desc">Homemade potato croquettes filled w/ smoked mozzarella</p></div>
    <div class="item"><div class="item-head"><span>Arancini (5)</span><span class="item-leader"></span><span class="item-price">$12.50</span></div><p class="item-desc">Sourdough crumbed rice balls with mixed wild mushrooms grana padano and gorgonzola emulsion</p></div>
    <div class="item"><div class="item-head"><span>Charred Brussels Sprouts</span><span class="item-leader"></span><span class="item-price">$10.50</span></div><p class="item-desc">Brussels sprouts with crispy parmesan flakes</p></div>
    <div class="item"><div class="item-head"><span>Homemade Fries</span><span class="item-leader"></span><span class="item-price">$8.50</span></div><p class="item-desc">House cut fries w/ your choice: classic, cajun spice or parmesan &amp; truffle</p></div>
    <div class="item"><div class="item-head"><span>Garlic Bread with Cheese</span><span class="item-leader"></span><span class="item-price">$6.50</span></div><p class="item-desc">Homemade garlic bread on fresh hearth-baked italian bread w/ side of marinara</p></div>
  </div>

  <div class="menu-section" style="left:32px;top:708px;width:380px">
    <h2 class="section-title">SALADS</h2>
    <div class="item"><div class="item-head"><span>The Market Bowl</span><span class="item-leader"></span><span class="item-price">$15.00</span></div><p class="item-desc">Romaine, tomatoes, corn, chickpeas, cucumbers, red onions, beets, carrots, avocado, pumpkin seeds, gorgonzola, shallot vinaigrette</p></div>
    <div class="item"><div class="item-head"><span>Sweet Greens</span><span class="item-leader"></span><span class="item-price">$14.00</span></div><p class="item-desc">Arugula, apples, walnuts, goat cheese, onion, red wine vinaigrette</p></div>
    <div class="item"><div class="item-head"><span>The Caesar</span><span class="item-leader"></span><span class="item-price">$12.00</span></div><p class="item-desc">Romaine, garlic croutons, parmesan, caesar dressing</p></div>
    <div class="item"><div class="item-head"><span>Huskers Harvest</span><span class="item-leader"></span><span class="item-price">$14.00</span></div><p class="item-desc">Shaved kale, shaved brussels sprouts, rainbow quinoa, carrots, cucumbers, sunflower seeds, red onions, dried cranberries, avocado, champagne vinaigrette</p></div>
    <div class="item"><div class="item-head"><span>Un-Feta-Getable Bowl</span><span class="item-leader"></span><span class="item-price">$14.00</span></div><p class="item-desc">Romaine, cucumbers, tomatoes, onions, kalamata olives, feta, greek dressing</p></div>
    <div class="item"><div class="item-head"><span>Go Green</span><span class="item-leader"></span><span class="item-price">$14.00</span></div><p class="item-desc">Spring greens, fennel, celery, pears, toasted almonds, basil, shaved parmesan, cracked pepper, olive oil, citrus vinaigrette</p></div>
    <div class="item"><div class="item-head"><span>Avo-Cobbo Bowl</span><span class="item-leader"></span><span class="item-price">$14.00</span></div><p class="item-desc">Romaine, tomatoes, cucumbers, chopped egg, avocado, red onions, shallot vinaigrette</p></div>
    <div class="item"><div class="item-head"><span>Midwest Foodie Bowl</span><span class="item-leader"></span><span class="item-price">$14.00</span></div><p class="item-desc">Romaine, corn, beans, pico de gallo, jack, avocado, chipotle ranch</p></div>
  </div>

  <div class="add-ons">
    <div class="add-on"><p class="add-on-title">TOPPINGS - $6<sup>50</sup></p><p>Grilled Chicken</p><p>Breaded Chicken Cutlet</p><p>Cajun Chicken</p></div>
    <div class="add-on"><p class="add-on-title">TOPPINGS - $7<sup>00</sup></p><p>Grilled Shrimp</p><p>Cajun Shrimp</p><p>Salmon</p><p>Sliced Skirt Steak</p></div>
  </div>

  <div class="menu-section" style="left:445px;top:245px;width:383px">
    <h2 class="section-title">PANINI OR WRAPS</h2>
    <p class="section-note">(SERVED WITH PICKLE &amp; FRIES)</p>
    <div class="item"><div class="item-head"><span>Burrata, Pesto, Tomatoes</span><span class="item-leader"></span><span class="item-price">$12.00</span></div><p class="item-desc">Tomatoes, basil pesto, burrata, arugula, olive oil, cracked salt and pepper, balsamic reduction</p></div>
    <div class="item"><div class="item-head"><span>Kickin' Cauliflower</span><span class="item-leader"></span><span class="item-price">$12.00</span></div><p class="item-desc">Crispy buffalo cauliflower, garlic sauteed kale, provolone, pickled jalapenos, garlic aioli</p></div>
    <div class="item"><div class="item-head"><span>King Caesar</span><span class="item-leader"></span><span class="item-price">$14.00</span></div><p class="item-desc">Cajun chicken, romaine, parmesan, caesar dressing</p></div>
    <div class="item"><div class="item-head"><span>Sca-More-Za Please!</span><span class="item-leader"></span><span class="item-price">$14.00</span></div><p class="item-desc">Caramelized onions, olives, basil, campari tomato, scamorza, evoo</p></div>
    <div class="item"><div class="item-head"><span>The Sizzler</span><span class="item-leader"></span><span class="item-price">$14.00</span></div><p class="item-desc">Chicken cutlet, bacon, fresh mozzarella, jalapenos, vodka sauce</p></div>
    <div class="item"><div class="item-head"><span>Not Cluckin' Around</span><span class="item-leader"></span><span class="item-price">$14.00</span></div><p class="item-desc">Grilled chicken, monterey jack, avocado, tomato, pesto aioli</p></div>
    <div class="item"><div class="item-head"><span>Great Bambino</span><span class="item-leader"></span><span class="item-price">$14.00</span></div><p class="item-desc">Grilled chicken, prosciutto, fresh mozzarella, tomatoes pesto aioli</p></div>
  </div>

  <div class="feature-box">
    <p class="feature-title">PARMIGIANA &amp; MILANESE</p>
    <p class="feature-style">Milanese Style: Baby Arugula, Red Onion, Tomato, Shaved Parmigiano, Aged Balsamic</p>
    <p class="feature-prices">CHICKEN $28<sup>75</sup> • JUMBO SHRIMP $33<sup>75</sup><br>EGGPLANT $28<sup>75</sup></p>
    <p class="feature-sub">Substitute Vodka Sauce $5<sup>25</sup></p>
  </div>

  <div class="menu-section" style="left:445px;top:708px;width:383px">
    <h2 class="section-title">ENTREES</h2>
    <div class="item"><div class="item-head"><span>Spaghetti Pesto alla Pollo</span><span class="item-leader"></span><span class="item-price">$19.50</span></div><p class="item-desc">Sauteed chicken breast, creamy basil pesto sauce &amp; parmesan</p></div>
    <div class="item"><div class="item-head"><span>Pasta w/ Meatballs</span><span class="item-leader"></span><span class="item-price">$16.00</span></div><p class="item-desc">Pasta w/ homemade meatballs &amp; marinara sauce</p></div>
    <div class="item"><div class="item-head"><span>Eggplant Parmigiana</span><span class="item-leader"></span><span class="item-price">$16.00</span></div><p class="item-desc">Nicely battered eggplant, marinara, mozzarella with side of spaghetti</p></div>
    <div class="item"><div class="item-head"><span>Penne Vodka</span><span class="item-leader"></span><span class="item-price">$16.00</span></div><p class="item-desc">Touch of cream, tomato sauce, splash of vodka</p></div>
    <div class="item"><div class="item-head"><span>Chicken Franchaise</span><span class="item-leader"></span><span class="item-price">$19.50</span></div><p class="item-desc">Lightly flour battered chicken breast sauteed in lemon white wine broth</p></div>
    <div class="item"><div class="item-head"><span>Chicken Parmigiana</span><span class="item-leader"></span><span class="item-price">$18.50</span></div><p class="item-desc">Breaded chicken cutlet, smokey tomato sauce, parmesan and mozzarella over spaghetti</p></div>
    <div class="item"><div class="item-head"><span>Chicken Scarpariello</span><span class="item-leader"></span><span class="item-price">$20.00</span></div><p class="item-desc">Chicken with italian sausage, olives, capers, mushrooms, and lightly spiced tomato sauce over honey garlic mashed potatoes</p></div>
    <div class="item"><div class="item-head"><span>Classic Shrimp Scampi</span><span class="item-leader"></span><span class="item-price">$21.50</span></div><p class="item-desc">Shrimp scampi with fresh arugula, diced tomatoes, splash of lemon</p></div>
    <div class="item"><div class="item-head"><span>Lasagna</span><span class="item-leader"></span><span class="item-price">$16.50</span></div><p class="item-desc">Our take on an italian classic</p></div>
    <div class="item"><div class="item-head"><span>Roasted Faroe Island Salmon</span><span class="item-leader"></span><span class="item-price">$25.50</span></div><p class="item-desc">Cherry tomatoes, capers, kalamata olives, marinara over sauteed veggies</p></div>
    <div class="item"><div class="item-head"><span>Thinly Sliced Skirt Steak</span><span class="item-leader"></span><span class="item-price">$25.50</span></div><p class="item-desc">Served with smokey slaw, crispy polenta, and chimichurri</p></div>
    <div class="item"><div class="item-head"><span>32-Hour Slow Roasted Short Rib</span><span class="item-leader"></span><span class="item-price">$25.50</span></div><p class="item-desc">Glazed cherry tomatoes with roasted potatoes and fresh rosemary</p></div>
  </div>

  <footer class="page-footer">
    <svg class="footer-band" viewBox="0 0 860 180" aria-hidden="true">
      <path fill="#111111" d="M0 180V36L24 26 48 34 70 14 96 30 120 20 150 34 180 22 210 36 240 26 280 40 320 30 360 44 400 34 440 46 480 38 520 48 560 36 600 44 640 30 680 40 720 22 750 32 780 12 810 26 835 8 860 18V180Z"/>
      <path fill="#fbf9f4" d="M60 40L160 34 158 38 62 44Z M300 44L420 40 418 44 302 48Z M660 36L760 26 758 30 662 40Z"/>
    </svg>
    <div class="contact-row">
      <span>Call Us - <span class="phone">847-318-5037</span></span>
      <span class="contact-item"><svg class="contact-icon" viewBox="0 0 16 16" aria-hidden="true"><rect x="1" y="1" width="14" height="14" fill="none" stroke="#e0121c" stroke-width="2"/><path d="M8 3.5a3 3 0 0 0-3 3c0 2.2 3 5.5 3 5.5s3-3.3 3-5.5a3 3 0 0 0-3-3z" fill="#e0121c"/></svg>8157 Tarrowell Avenue Alder Ridge, NY 12831</span>
      <span class="contact-item"><svg class="contact-icon" viewBox="0 0 16 16" aria-hidden="true"><rect x="1" y="1" width="14" height="14" fill="none" stroke="#e0121c" stroke-width="2"/><circle cx="8" cy="8" r="3.5" fill="none" stroke="#e0121c" stroke-width="1.5"/></svg>Ovenbellhub.com</span>
    </div>
    <div class="hours"><span class="hours-days">MONDAY - SUNDAY</span><span class="hours-time">11AM - 9PM</span></div>
  </footer>
</section>

<!-- Page two: pizza, toppings and desserts -->
<section class="menu-page menu-page--pizza">
  <header class="page-header">
    <svg class="header-band" viewBox="0 0 860 250" aria-hidden="true">
      <defs>
        <linearGradient id="redPizza" x1="0" y1="0" x2="1" y2="1">
          <stop offset="0" stop-color="#c8000c"/><stop offset=".5" stop-color="#e31520"/><stop offset="1" stop-color="#b5000a"/>
        </linearGradient>
      </defs>
      <path fill="url(#redPizza)" d="M0 0H860V170L830 180 800 174 770 190 740 182 700 198 660 190 620 204 580 196 540 210 500 202 460 216 420 206 380 222 340 212 300 228 260 218 220 232 180 222 140 238 100 228 60 244 30 234 0 248Z"/>
      <path fill="#fbf9f4" d="M120 236L240 212 238 216 126 240Z M420 210L560 192 556 196 424 214Z M640 194L760 178 758 182 644 198Z"/>
    </svg>
    <div class="brand-name">Ovenbell</div>
    <div class="pizza-kicker">Pizza</div>
    <div class="pizza-title">Menu</div>
    <div class="food-photo food-photo--pizza" role="img" aria-label="Photo of two whole pizzas with flying pizza slices"></div>
  </header>

  <div class="menu-section pizza-list" style="left:40px;top:296px;width:380px">
    <h2 class="section-title">PIZZA</h2>
    <div class="item"><div class="item-head"><span>The Big Cheese</span><span class="item-leader"></span><span class="item-price">$17.00<small>LARGE</small>/14.00<small>PER</small></span></div><p class="item-desc">Classic new york pizza, topped with tomato sauce and mozzarella</p></div>
    <div class="item"><div class="item-head"><span>Hot Stuff</span><span class="item-leader"></span><span class="item-price">$21.00<small>LARGE</small>/15.00<small>PER</small></span></div><p class="item-desc">Chicken cutlet marinated in hot sauce, topped with homemade ranch dressing drizzle</p></div>
    <div class="item"><div class="item-head"><span>BBQ Special</span><span class="item-leader"></span><span class="item-price">$21.00<small>LARGE</small>/15.00<small>PER</small></span></div><p class="item-desc">Chicken cutlet marinated in tangy barbeque sauce</p></div>
    <div class="item"><div class="item-head"><span>Pizza Margherita</span><span class="item-leader"></span><span class="item-price">$21.00<small>LARGE</small>/15.00<small>PER</small></span></div><p class="item-desc">Margherita style pizza - topped with san marzano tomatoes, basil, mozzarella and olive oil drizzle</p></div>
    <div class="item"><div class="item-head"><span>Great White</span><span class="item-leader"></span><span class="item-price">$21.00<small>LARGE</small>/15.00<small>PER</small></span></div><p class="item-desc">Battered eggplant coated in homemade tomato sauce, mozzarella, parmesan and ricotta</p></div>
    <div class="item"><div class="item-head"><span>Eggplant Delight</span><span class="item-leader"></span><span class="item-price">$21.00<small>LARGE</small>/15.00<small>PER</small></span></div><p class="item-desc">Classic new york pizza, topped with tomato sauce and mozzarella</p></div>
    <div class="item"><div class="item-head"><span>Chicken Club</span><span class="item-leader"></span><span class="item-price">$21.00<small>LARGE</small>/15.00<small>PER</small></span></div><p class="item-desc">Breaded chicken cutlet coated in homemade tomato sauce, mozzarella, parmesan and ricotta</p></div>
    <div class="item"><div class="item-head"><span>Classic Chicken Francese</span><span class="item-leader"></span><span class="item-price">$21.00<small>LARGE</small>/15.00<small>PER</small></span></div><p class="item-desc">Battered chicken breast sauteed in lemon white wine broth</p></div>
    <div class="item"><div class="item-head"><span>Hot Links</span><span class="item-leader"></span><span class="item-price">$22.00<small>LARGE</small>/16.00<small>PER</small></span></div><p class="item-desc">Crumbled hot sausage and vodka sauce</p></div>
    <div class="item"><div class="item-head"><span>Ulti-Meat</span><span class="item-leader"></span><span class="item-price">$22.00<small>LARGE</small>/16.00<small>PER</small></span></div><p class="item-desc">Mozzarella, pastrami, salami, meatballs, creamy ricotta, chives, hot sausage, basil, caramelized onions, hot peppers</p></div>
    <div class="item"><div class="item-head"><span>The Prosciutto*</span><span class="item-leader"></span><span class="item-price">$22.00<small>LARGE</small>/16.00<small>PER</small></span></div><p class="item-desc">Prosciutto di parma, arugula, fresh mozzarella</p></div>
    <div class="item"><div class="item-head"><span>Get Em to the Greek!</span><span class="item-leader"></span><span class="item-price">$22.00<small>LARGE</small>/16.00<small>PER</small></span></div><p class="item-desc">Red onions, tomatoes, aromatic oregano, greek olives, feta cheese</p></div>
    <div class="item"><div class="item-head"><span>Veggie Supreme*</span><span class="item-leader"></span><span class="item-price">$22.00<small>LARGE</small>/16.00<small>PER</small></span></div><p class="item-desc">Tomatoes, smoked mozzarella, seasonal vegetables, olives, capers, evoo</p></div>
    <div class="item"><div class="item-head"><span>Ricotta Be Kidding Me!</span><span class="item-leader"></span><span class="item-price">$22.00<small>LARGE</small>/16.00<small>PER</small></span></div><p class="item-desc">Ricotta, roasted garlic, charred baby broccoli, fresh mozzarella</p></div>
    <div class="item"><div class="item-head"><span>Lots of Shrooms*</span><span class="item-leader"></span><span class="item-price">$22.00<small>LARGE</small>/16.00<small>PER</small></span></div><p class="item-desc">Fresh mozzarella, cream of mushrooms, mushrooms, arugula, truffle oil, parmesan</p></div>
    <div class="item"><div class="item-head"><span>Pizza My Heart</span><span class="item-leader"></span><span class="item-price">$22.00<small>LARGE</small>/16.00<small>PER</small></span></div><p class="item-desc">Zucchini squash, artichoke hearts, garlic, fresh basil, oil, shaved parmesan</p></div>
    <div class="item"><div class="item-head"><span>Veggiemore*</span><span class="item-leader"></span><span class="item-price">$22.00<small>LARGE</small>/16.00<small>PER</small></span></div><p class="item-desc">Eggplant, zucchini, roasted peppers, fresh mozzarella, san marzano tomato sauce</p></div>
    <div class="item"><div class="item-head"><span>Shrimp Pancetta*</span><span class="item-leader"></span><span class="item-price">$22.00<small>LARGE</small>/16.00<small>PER</small></span></div><p class="item-desc">Shrimp, pancetta, arugula, fresh mozzarella, shaved parmesan, balsamic reduction</p></div>
    <div class="item"><div class="item-head"><span>The Sicilian</span><span class="item-leader"></span><span class="item-price">$19.00<small>LARGE</small></span></div><p class="item-desc">Traditional thick crust sicilian style topped with tomato sauce and mozzarella</p></div>
    <div class="item"><div class="item-head"><span>Grandma Pie</span><span class="item-leader"></span><span class="item-price">$23.00<small>LARGE</small></span></div><p class="item-desc">Thin crust topped with marinated tomato, fresh mozzarella, basil and garlic</p></div>
    <div class="item"><div class="item-head"><span>Drunken Grandma</span><span class="item-leader"></span><span class="item-price">$23.00<small>LARGE</small></span></div><p class="item-desc">Crispy grandma style, topped with vodka sauce, fresh mozzarella, romano and fresh basil</p></div>
  </div>

  <div class="menu-section topping-list" style="left:440px;top:296px;width:380px">
    <h2 class="section-title">PIZZA TOPPINGS</h2>
    <div class="item"><div class="item-head"><span>The Big Cheese</span><span class="item-leader"></span><span class="item-price">$4.50</span></div></div>
    <div class="item"><div class="item-head"><span>Anchovies</span><span class="item-leader"></span><span class="item-price">$4.50</span></div></div>
    <div class="item"><div class="item-head"><span>Artichoke Hearts</span><span class="item-leader"></span><span class="item-price">$4.50</span></div></div>
    <div class="item"><div class="item-head"><span>Bacon</span><span class="item-leader"></span><span class="item-price">$4.50</span></div></div>
    <div class="item"><div class="item-head"><span>Black Olives</span><span class="item-leader"></span><span class="item-price">$4.50</span></div></div>
    <div class="item"><div class="item-head"><span>Broccoli</span><span class="item-leader"></span><span class="item-price">$4.50</span></div></div>
    <div class="item"><div class="item-head"><span>Egg Plant</span><span class="item-leader"></span><span class="item-price">$4.50</span></div></div>
    <div class="item"><div class="item-head"><span>Extra Cheese</span><span class="item-leader"></span><span class="item-price">$4.50</span></div></div>
    <div class="item"><div class="item-head"><span>Fresh Garlic</span><span class="item-leader"></span><span class="item-price">$4.50</span></div></div>
    <div class="item"><div class="item-head"><span>Fresh Mushrooms</span><span class="item-leader"></span><span class="item-price">$4.50</span></div></div>
    <div class="item"><div class="item-head"><span>Green Peppers</span><span class="item-leader"></span><span class="item-price">$4.50</span></div></div>
    <div class="item"><div class="item-head"><span>Hot Cherry Peppers</span><span class="item-leader"></span><span class="item-price">$4.50</span></div></div>
  </div>

  <div class="menu-section dessert-list" style="left:444px;top:708px;width:380px">
    <h2 class="section-title">DESSERTS</h2>
    <div class="item" style="margin-top:26px"><div class="item-head"><span>Plain Nocciola Crepe</span><span class="item-leader"></span><span class="item-price">$9.00</span></div></div>
    <div class="item"><div class="item-head"><span>Banana +</span><span class="item-leader"></span><span class="item-price">$4.50</span></div><p class="item-desc">Fire roasted marshmello &amp; nocciola</p></div>
    <div class="item"><div class="item-head"><span>Strawberry +</span><span class="item-leader"></span><span class="item-price">$4.50</span></div><p class="item-desc">Fire roasted marshmello &amp; nocciola</p></div>
    <div class="item"><div class="item-head"><span>Strawberry +</span><span class="item-leader"></span><span class="item-price">$4.50</span></div><p class="item-desc">Fire roasted marshmello &amp; nocciola</p></div>
    <div class="item"><div class="item-head"><span>Banana + Strawberry +</span><span class="item-leader"></span><span class="item-price">$4.50</span></div><p class="item-desc">Fire roasted marshmello &amp; nocciola</p></div>
    <div class="item"><div class="item-head"><span>Wild Berries +</span><span class="item-leader"></span><span class="item-price">$4.50</span></div><p class="item-desc">Fire roasted marshmello &amp; nocciola</p></div>
    <div class="item"><div class="item-head"><span>Mixed Fruits +</span><span class="item-leader"></span><span class="item-price">$4.50</span></div><p class="item-desc">Fire roasted marshmello &amp; nocciola</p></div>
    <div class="item"><div class="item-head"><span>Peanut Butter + Banana +</span><span class="item-leader"></span><span class="item-price">$4.50</span></div><p class="item-desc">Fire roasted marshmello &amp; nocciola</p></div>
    <div class="item"><div class="item-head"><span>Cinnamon + Apple + Brown Sugar +</span><span class="item-leader"></span><span class="item-price">$4.50</span></div><p class="item-desc">Fire roasted marshmello &amp; nocciola</p></div>
  </div>

  <footer class="page-footer">
    <svg class="footer-band" viewBox="0 0 860 180" aria-hidden="true">
      <path fill="#111111" d="M0 180V36L24 26 48 34 70 14 96 30 120 20 150 34 180 22 210 36 240 26 280 40 320 30 360 44 400 34 440 46 480 38 520 48 560 36 600 44 640 30 680 40 720 22 750 32 780 12 810 26 835 8 860 18V180Z"/>
      <path fill="#fbf9f4" d="M60 40L160 34 158 38 62 44Z M300 44L420 40 418 44 302 48Z M660 36L760 26 758 30 662 40Z"/>
    </svg>
    <div class="contact-row">
      <span>Call Us - <span class="phone">847-318-5037</span></span>
      <span class="contact-item"><svg class="contact-icon" viewBox="0 0 16 16" aria-hidden="true"><rect x="1" y="1" width="14" height="14" fill="none" stroke="#e0121c" stroke-width="2"/><path d="M8 3.5a3 3 0 0 0-3 3c0 2.2 3 5.5 3 5.5s3-3.3 3-5.5a3 3 0 0 0-3-3z" fill="#e0121c"/></svg>8157 Tarrowell Avenue Alder Ridge, NY 12831</span>
      <span class="contact-item"><svg class="contact-icon" viewBox="0 0 16 16" aria-hidden="true"><rect x="1" y="1" width="14" height="14" fill="none" stroke="#e0121c" stroke-width="2"/><circle cx="8" cy="8" r="3.5" fill="none" stroke="#e0121c" stroke-width="1.5"/></svg>Ovenbellhub.com</span>
    </div>
    <div class="hours"><span class="hours-days">MONDAY - SUNDAY</span><span class="hours-time">11AM - 9PM</span></div>
  </footer>
</section>

</body>
</html>
```